Balance Pack Redesign Wordpress site

IMPORTANT: the design will need to look nice on mobile...so please keep that in mind!
We need to redesign our current Wordpress page to make it more appealing and look like an ecommerce page. We need the ability to implement this design on our Wordpress site.

Here is the current page: https://www.kalvoreaonline.com/supplements/balance-core-pack/

However, the reference sample of what it has to look like or complement is also attached.

Attached is the Word document is the copy for the new page and the FAQs text.

The color palette is attached but focus primarily on the GREEN COLOR as the pink color will be for the next page that gets designed.

Thanks!

Target Market(s)

women over 40 struggling with hormonal imbalances

Industry/Entity Type

health and wellness

Requirements
Must have
• requirements attached.
Nice to have
• my pics included in dropbox link
Should not have
• NO RANDOM Stock Photography of people, only use images in dropbox

```html
<!DOCTYPE html>
<html lang="en">
<head>
<meta charset="utf-8">
<title>Balance Core Pack</title>
<link href="https://fonts.googleapis.com/css2?family=Poppins:wght@400;500;600;700;800&display=swap" rel="stylesheet">
<style>
:root{
  --stage:#6a6a6a;
  --green-dark:#2d5e3e;
  --green:#3f8a58;
  --green-mid:#6fae7f;
  --green-soft:#cfe6d2;
  --green-pale:#eef6ee;
  --ink:#1d2a22;
  --muted:#5d6b62;
  --white:#ffffff;
  --photo-a:#c9b8a6;
  --photo-b:#a9c7b0;
  --line:#d9e4da;
  --gold:#d8b24a;
}
*{box-sizing:border-box;margin:0;padding:0}
html,body{width:1200px;height:2644px;overflow:hidden}
body{background:var(--stage);font-family:"Poppins",sans-serif;color:var(--ink);position:relative}
.page{position:absolute;top:16px;width:560px;background:var(--white);overflow:hidden}
.page--left{left:30px}
.page--right{left:610px}
.photo{background:linear-gradient(150deg,var(--photo-a),var(--photo-b))}
.product{background:linear-gradient(160deg,#ffffff,#dfeee0)}
h2{font-size:22px;font-weight:700;line-height:1.15;color:var(--ink)}
h2 .accent{color:var(--green)}
p{font-size:8px;line-height:1.5;color:var(--muted)}
.btn{display:inline-block;background:var(--green-dark);color:var(--white);font-size:8px;font-weight:600;padding:6px 14px;border-radius:14px;white-space:nowrap}
.tag{display:inline-block;background:var(--green);color:var(--white);font-size:8px;font-weight:600;padding:4px 10px;border-radius:3px;white-space:nowrap;flex:none}
.ticks{list-style:none}
.ticks li{font-size:7.5px;line-height:1.5;color:var(--ink);padding-left:12px;position:relative;margin-bottom:3px}
.ticks li::before{content:"";position:absolute;left:0;top:3px;width:6px;height:6px;border-radius:50%;background:var(--green)}

/* header */
.site-header{height:44px;display:flex;align-items:center;padding:0 22px;gap:18px;border-bottom:1px solid var(--line)}
.brand{font-size:11px;font-weight:700;color:var(--green-dark);letter-spacing:1px;display:flex;align-items:center;gap:5px}
.brand::before{content:"";width:8px;height:8px;border-radius:50%;background:var(--green)}
.nav{display:flex;gap:12px;font-size:6.5px;color:var(--muted)}
.header-actions{margin-left:auto;display:flex;gap:6px}
.header-actions span{font-size:6px;padding:4px 8px;border-radius:10px;background:var(--green);color:#fff}
.header-actions span + span{background:var(--green-pale);color:var(--green-dark)}

/* hero */
.hero{height:295px;position:relative;background:linear-gradient(90deg,var(--white) 45%,var(--green-pale));padding:44px 24px}
.hero h1{font-size:28px;font-weight:800;line-height:1.1;width:250px}
.hero h3{font-size:13px;font-weight:600;color:var(--green);line-height:1.3;width:240px;margin:12px 0 16px}
.hero-rings{position:absolute;right:24px;top:30px;width:240px;height:240px;border-radius:50%;background:var(--green-soft);display:flex;align-items:center;justify-content:center}
.hero-rings::before{content:"";position:absolute;inset:18px;border-radius:50%;background:var(--green-mid)}
.hero-rings .product{position:relative;width:160px;height:160px;border-radius:50%}

/* not alone */
.not-alone{height:258px;display:flex;align-items:center;gap:26px;padding:0 24px}
.ring-photo{flex:none;border-radius:50%;border:8px solid var(--green-soft);box-shadow:0 0 0 5px var(--green)}
.not-alone .ring-photo{width:170px;height:170px}
.not-alone h2{font-size:15px;margin-bottom:8px}
.not-alone p{margin-bottom:6px}

/* why */
.why{height:616px;padding:16px 24px 0;text-align:center}
.why h2{font-size:19px}
.why .sub{font-size:10px;font-weight:600;color:var(--green);margin:3px 0 18px}
.why-row{display:flex;align-items:center;gap:20px;text-align:left;height:165px}
.why-row.reverse{flex-direction:row-reverse}
.why-row .ring-photo{width:125px;height:125px}
.why-row h4{font-size:10px;font-weight:700;margin-bottom:6px}
.why-row h4 small{font-weight:400;font-size:7px;color:var(--muted)}
.why-row .btn{margin-top:6px}

/* results */
.results{height:257px;background:var(--green-pale);padding:30px 24px;text-align:center}
.results h2{font-size:22px}
.results-strip{display:flex;gap:8px;margin-top:18px;justify-content:center}
.results-strip div{width:92px;height:110px;border-radius:6px}
.dots{display:flex;gap:5px;justify-content:center;margin-top:12px}
.dots span{width:6px;height:6px;border-radius:50%;background:var(--line)}
.dots span:first-child{background:var(--green)}

/* science */
.science{height:1093px;padding:30px 24px;}
.science-head{text-align:center}
.science-head h2{font-size:22px}
.science-head h5{font-size:10px;font-weight:600;color:var(--green);margin:8px 0 4px}
.study{margin-top:22px}
.study h4{font-size:11px;font-weight:700;margin:10px 0 8px}
.chart{background:var(--white);border:1px solid var(--line);border-radius:4px;margin:0 auto 10px;display:block}
.takeaways h6{font-size:8px;font-weight:700;margin:8px 0 4px}

/* right: difference */
.difference{height:380px;background:linear-gradient(160deg,var(--green-dark),var(--green));color:#fff;padding:34px 24px;position:relative}
.difference h2{color:#fff;font-size:22px;width:300px}
.difference .ticks{margin-top:16px;width:300px}
.difference .ticks li{color:#eaf4ea;font-size:7.5px;margin-bottom:6px}
.difference .ticks li::before{background:#cfe6d2}
.difference .ring-photo{position:absolute;right:24px;top:40px;width:190px;height:190px;border-color:var(--green-mid);box-shadow:0 0 0 5px #fff}

.study3{height:395px;padding:26px 24px}
.study3 .intro{display:flex;gap:10px;align-items:flex-start}

.compare{height:273px;padding:22px 24px;text-align:center}
.compare h2{font-size:18px}
.compare table{width:100%;border-collapse:collapse;margin:14px 0 10px;text-align:left}
.compare th{font-size:7px;background:var(--green-dark);color:#fff;padding:5px;font-weight:600}
.compare td{font-size:6.5px;color:var(--muted);padding:5px;border:1px solid var(--line);line-height:1.4}
.compare tr:nth-child(even) td{background:var(--green-pale)}

.offer{height:187px;background:linear-gradient(90deg,var(--green-dark),var(--green));display:flex;align-items:flex-end;padding:0 24px;gap:22px;color:#fff;position:relative}
.offer .photo{width:140px;height:175px;border-radius:70px 70px 0 0;flex:none}
.offer-copy{align-self:center}
.offer-copy h3{font-size:22px;font-weight:700}
.offer-copy h4{font-size:12px;font-weight:600;margin:4px 0}
.offer-copy p{color:#e1efe2;width:230px}
.offer-copy .price{font-size:10px;font-weight:700;color:var(--gold);margin:4px 0 8px}
.offer-copy .btn{background:#fff;color:var(--green-dark)}
.seal{position:absolute;right:26px;top:58px;width:58px;height:58px;border-radius:50%;background:var(--gold)}

.faq{height:634px;padding:30px 24px;position:relative;overflow:hidden}
.faq h2{text-align:center;font-size:20px;margin-bottom:18px}
.faq-list{width:330px}
.faq-item{border:1px solid var(--line);border-radius:3px;padding:7px 10px;font-size:7px;font-weight:600;margin-bottom:7px;display:flex;justify-content:space-between}
.faq-item::after{content:"+";color:var(--green)}
.faq-item.open{background:var(--green-pale);flex-wrap:wrap}
.faq-item.open::after{content:"–"}
.faq-item.open p{flex-basis:100%;font-weight:400;margin-top:4px;order:3}
.faq-visual{position:absolute;right:0;top:150px;width:180px;height:300px;border-radius:150px 0 0 150px;border:8px solid var(--green-soft);border-right:none}

.reviews{height:550px;padding:40px 24px;text-align:center}
.reviews h2{font-size:18px;font-weight:600;letter-spacing:.5px}
.reviews .slot{font-size:11px;font-weight:700;color:var(--green-dark);margin-top:8px}

.site-footer{height:168px;background:var(--green-pale);padding:26px 24px;text-align:center}
.site-footer .brand{justify-content:center;font-size:14px}
.footer-cols{display:flex;justify-content:space-between;margin:16px 0 14px;font-size:6.5px;color:var(--muted)}
.footer-cols div{display:flex;align-items:center;gap:5px}
.footer-cols i{width:14px;height:14px;border-radius:50%;background:var(--green);display:inline-block}
.footer-base{font-size:6px;color:var(--muted);border-top:1px solid var(--line);padding-top:10px}
</style>
</head>
<body>

<main class="page page--left">
  <header class="site-header">
    <div class="brand">KALVOREA</div>
    <nav class="nav"><span>Shop All</span><span>Weight Loss</span><span>Hormones</span><span>Programs</span><span>About</span></nav>
    <div class="header-actions"><span>Shop Now</span><span>Account</span></div>
  </header>

  <section class="hero">
    <h1>The Balance Core Pack</h1>
    <h3>The Complete Solution for Hormonal Balance &amp; Well-Being</h3>
    <span class="btn">SHOP NOW</span>
    <div class="hero-rings"><div class="product" role="img" aria-label="Balance Core and LunaBalm product bottles"></div></div>
  </section>

  <section class="not-alone">
    <div class="ring-photo photo" role="img" aria-label="Smiling woman holding the supplement"></div>
    <div>
      <h2>It's Not Just in Your Head…<br><span class="accent">And You're Not Alone.</span></h2>
      <p>Hot flashes, mood swings, stubborn weight and restless nights are signs your hormones may be out of balance. Millions of women over 40 feel the same shifts every day.</p>
      <p>The good news is that support is simple. Two targeted formulas work together to help your body restore a calm, steady rhythm.</p>
      <ul class="ticks">
        <li>Supports healthy estrogen metabolism naturally</li>
        <li>Helps ease everyday mood swings and irritability</li>
        <li>Promotes restful sleep and steady daily energy</li>
        <li>Supports a balanced, comfortable monthly cycle</li>
      </ul>
    </div>
  </section>

  <section class="why">
    <h2>Why Use Both?</h2>
    <div class="sub">The Synergy of Balance Core &amp; LunaBalm Pack</div>

    <div class="why-row reverse">
      <div class="ring-photo photo" role="img" aria-label="Woman holding Balance Core bottle"></div>
      <div>
        <h4>Balance Core <small>Capsules · Estrogen Metabolism Support</small></h4>
        <ul class="ticks">
          <li>Supports healthy estrogen detoxification</li>
          <li>Helps reduce bloating and water retention</li>
          <li>Encourages balanced mood and clear focus</li>
          <li>Promotes healthy skin and steady weight</li>
        </ul>
        <span class="btn">SHOP BALANCE CORE</span>
      </div>
    </div>

    <div class="why-row">
      <div class="ring-photo photo" role="img" aria-label="Woman applying LunaBalm cream"></div>
      <div>
        <h4>LunaBalm <small>Topical Cream · Natural Progesterone Support</small></h4>
        <ul class="ticks">
          <li>Balances estrogen dominance with gentle support</li>
          <li>Supports calm, restful nights of sleep</li>
          <li>Helps ease hot flashes and night sweats</li>
          <li>Promotes a comfortable, regular cycle</li>
        </ul>
        <span class="btn">SHOP LUNABALM</span>
      </div>
    </div>

    <div class="why-row reverse">
      <div class="ring-photo photo" role="img" aria-label="Woman holding both products together"></div>
      <div>
        <h4>Better Together</h4>
        <p>When used together, the two formulas address both sides of hormone balance: clearing excess estrogen while replenishing progesterone for complete, lasting support.</p>
        <span class="btn">SHOP THE PACK</span>
      </div>
    </div>
  </section>

  <section class="results">
    <h2>Real Women<br><span class="accent">Real Results</span></h2>
    <div class="results-strip">
      <div class="photo" role="img" aria-label="Customer photo one"></div>
      <div class="photo" role="img" aria-label="Customer photo two"></div>
      <div class="photo" role="img" aria-label="Customer photo three"></div>
      <div class="photo" role="img" aria-label="Customer photo four"></div>
      <div class="photo" role="img" aria-label="Customer photo five"></div>
    </div>
    <div class="dots"><span></span><span></span><span></span></div>
  </section>

  <section class="science">
    <div class="science-head">
      <h2>Backed by Science<br><span class="accent">See How It Works</span></h2>
      <h5>The Power of Brassica Extract &amp; Calcium D-Glucarate</h5>
      <p>Key ingredients studied for their role in healthy estrogen metabolism.</p>
    </div>

    <div class="study">
      <span class="tag">Study #1</span>
      <h4>Brassica Extract Supports Healthy Estrogen Metabolism</h4>
      <svg class="chart" width="300" height="200" viewBox="0 0 300 200" role="img" aria-label="Bar chart of estrogen metabolite ratio">
        <text x="150" y="18" font-size="8" text-anchor="middle" font-family="Poppins" font-weight="600" fill="#1d2a22">Effect on Estrogen Metabolite Ratio</text>
        <line x1="40" y1="170" x2="280" y2="170" stroke="#999"/>
        <line x1="40" y1="30" x2="40" y2="170" stroke="#999"/>
        <rect x="80" y="120" width="50" height="50" fill="#6fae7f"/>
        <rect x="180" y="50" width="50" height="120" fill="#2d5e3e"/>
        <text x="105" y="184" font-size="7" text-anchor="middle" fill="#5d6b62">Placebo</text>
        <text x="205" y="184" font-size="7" text-anchor="middle" fill="#5d6b62">Brassica</text>
      </svg>
      <p>Women taking the extract showed a clear shift toward healthier estrogen metabolites compared to placebo over the study period.</p>
      <div class="takeaways">
        <h6>Key Takeaways from the Study</h6>
        <ul class="ticks">
          <li>Improved ratio of protective estrogen metabolites</li>
          <li>Well tolerated with no reported side effects</li>
        </ul>
      </div>
    </div>

    <div class="study">
      <span class="tag">Study #2</span>
      <h4>Calcium D-Glucarate Supports Estrogen Detoxification</h4>
      <svg class="chart" width="340" height="230" viewBox="0 0 340 230" role="img" aria-label="Bar chart of detoxification enzyme activity">
        <text x="170" y="18" font-size="8" text-anchor="middle" font-family="Poppins" font-weight="600" fill="#1d2a22">Enzyme Activity by Group</text>
        <line x1="40" y1="200" x2="320" y2="200" stroke="#999"/>
        <line x1="40" y1="30" x2="40" y2="200" stroke="#999"/>
        <rect x="65" y="60" width="26" height="140" fill="#2d5e3e"/><rect x="93" y="150" width="26" height="50" fill="#6fae7f"/>
        <rect x="155" y="90" width="26" height="110" fill="#2d5e3e"/><rect x="183" y="160" width="26" height="40" fill="#6fae7f"/>
        <rect x="245" y="110" width="26" height="90" fill="#2d5e3e"/><rect x="273" y="170" width="26" height="30" fill="#6fae7f"/>
        <text x="92" y="214" font-size="7" text-anchor="middle" fill="#5d6b62">Week 4</text>
        <text x="182" y="214" font-size="7" text-anchor="middle" fill="#5d6b62">Week 8</text>
        <text x="272" y="214" font-size="7" text-anchor="middle" fill="#5d6b62">Week 12</text>
      </svg>
      <div class="takeaways">
        <h6>Key Takeaways from the Study</h6>
        <ul class="ticks">
          <li>Supported the body's natural clearance of excess estrogen</li>
          <li>Consistent benefits across all measured weeks</li>
          <li>Pairs well with progesterone support for full balance</li>
        </ul>
      </div>
    </div>
  </section>
</main>

<main class="page page--right">
  <section class="difference">
    <h2>The LunaBalm Difference<br>More Than Just Progesterone</h2>
    <ul class="ticks">
      <li>Bioidentical progesterone in a soothing, fast-absorbing cream</li>
      <li>Added botanicals to calm skin and support relaxation</li>
      <li>Easy measured dose for consistent daily use</li>
      <li>Free from parabens, fragrance and harsh fillers</li>
      <li>Made in the USA in a certified facility</li>
    </ul>
    <div class="ring-photo photo" role="img" aria-label="Woman holding LunaBalm jar"></div>
  </section>

  <section class="study3">
    <div class="intro">
      <span class="tag">Study #3</span>
      <p>Below is an illustrative representation summarizing the potential benefits of topical progesterone cream based on the studies.</p>
    </div>
    <svg class="chart" style="margin-top:16px" width="380" height="250" viewBox="0 0 380 250" role="img" aria-label="Bar chart of symptom improvement">
      <text x="190" y="18" font-size="8" text-anchor="middle" font-family="Poppins" font-weight="600" fill="#1d2a22">Symptom Relief with Topical Progesterone</text>
      <line x1="40" y1="215" x2="360" y2="215" stroke="#999"/>
      <line x1="40" y1="30" x2="40" y2="215" stroke="#999"/>
      <rect x="70" y="150" width="30" height="65" fill="#c9c9c9"/><rect x="102" y="50" width="30" height="165" fill="#2d5e3e"/>
      <rect x="170" y="160" width="30" height="55" fill="#c9c9c9"/><rect x="202" y="70" width="30" height="145" fill="#2d5e3e"/>
      <rect x="270" y="165" width="30" height="50" fill="#c9c9c9"/><rect x="302" y="80" width="30" height="135" fill="#2d5e3e"/>
      <text x="101" y="230" font-size="7" text-anchor="middle" fill="#5d6b62">Hot Flashes</text>
      <text x="201" y="230" font-size="7" text-anchor="middle" fill="#5d6b62">Sleep Quality</text>
      <text x="301" y="230" font-size="7" text-anchor="middle" fill="#5d6b62">Mood</text>
    </svg>
  </section>

  <section class="compare">
    <h2>Which Hormone Products Are Right For You?<br><span class="accent">Find Your Perfect Hormone Balance</span></h2>
    <table>
      <tr><th>Product</th><th>Best For</th><th>How It Works</th><th>Use</th></tr>
      <tr><td>Balance Core</td><td>Bloating, weight, mood</td><td>Clears excess estrogen</td><td>2 capsules daily</td></tr>
      <tr><td>LunaBalm</td><td>Sleep, hot flashes</td><td>Restores progesterone</td><td>Apply once daily</td></tr>
      <tr><td>Balance Pack</td><td>Complete support</td><td>Works on both sides</td><td>Use together daily</td></tr>
    </table>
    <span class="btn">FIND THE BALANCE FOR YOU</span>
  </section>

  <section class="offer">
    <div class="photo" role="img" aria-label="Woman holding the two products"></div>
    <div class="offer-copy">
      <h3>Special Offer</h3>
      <h4>Bundle &amp; Save!</h4>
      <p>Get both products at one special price when you buy together.</p>
      <div class="price">$89.99 value · now $79.99</div>
      <span class="btn">SHOP NOW</span>
    </div>
    <div class="seal" role="img" aria-label="Guarantee seal"></div>
  </section>

  <section class="faq">
    <h2>Frequently Asked Questions</h2>
    <div class="faq-list">
      <div class="faq-item open">Why should I use both products together?<p>They support both sides of hormone balance, clearing excess estrogen while restoring progesterone for fuller relief.</p></div>
      <div class="faq-item">How long before I notice results?</div>
      <div class="faq-item">Can I use these during perimenopause?</div>
      <div class="faq-item">Are there any side effects?</div>
      <div class="faq-item">Where do I apply the cream?</div>
      <div class="faq-item">Can I take these with other supplements?</div>
      <div class="faq-item">Is the progesterone bioidentical?</div>
      <div class="faq-item">How much cream should I use each day?</div>
      <div class="faq-item">Do I need to cycle off the products?</div>
      <div class="faq-item">Are the products safe after menopause?</div>
      <div class="faq-item">What is your return policy?</div>
      <div class="faq-item">How should I store the products?</div>
    </div>
    <div class="faq-visual product" role="img" aria-label="Product bottles on green backdrop"></div>
  </section>

  <section class="reviews">
    <h2>CUSTOMER REVIEWS</h2>
    <div class="slot">SPACE for Revuo Reviews</div>
  </section>

  <footer class="site-footer">
    <div class="brand">KALVOREA</div>
    <div class="footer-cols">
      <div><i></i>(555) 014-2290</div>
      <div><i></i>help@kalvoreaonline.com</div>
      <div><i></i>120 Meadow Lane, Suite 4</div>
    </div>
    <div class="footer-base">© Kalvorea. All rights reserved. · Privacy Policy · Terms of Service</div>
  </footer>
</main>

</body>
</html>
```